Infografiken für Rechtsfirma
Zielgruppe
Wir sind eine Rechtsfirma, welche sich mit dem europäischen Recht beschäftigt. Wir bieten Insolvenzen in unterschiedlichen Ländern an. Weiter beraten wir hinsichtlich des Vermögensschutzes. Wir helfen dabei, Vermögenswerte zu sichern. Für unseren Bereich Vermögensschutz benötigen wir eine Grafik, welche die Vorteile unseres Produkts direkt auf einen Blick erkennen lässt. Hierzu habe ich eine Grafik eines großen Mobilfunkherstellers beigefügt. Im gleichen Designe möchten wir diese Grafik haben.
Aufgabenstellung
Ich habe eine PDF-Datei (Vermögensschutz) beigefügt, aus welcher sich die Keyfacts ergeben. Diese müssen grafisch aufbereitet werden.

```html
<!DOCTYPE html>
<html lang="de">
<head>
<meta charset="utf-8">
<title>Vermögensschutz – Vorteile auf einen Blick</title>
<link rel="stylesheet" href="https://fonts.googleapis.com/css2?family=Catamaran:wght@400;700&family=Poppins:wght@800&display=swap">
<style>
  :root {
    --bg: #ffffff;
    --accent: #7a50cf;
    --body-text: #1f1f24;
    --disc-deep: #7350d3;
    --disc-light: #9b72df;
    --badge: #ffffff;
  }
  * { margin: 0; padding: 0; box-sizing: border-box; }
  html, body { width: 1200px; height: 1200px; overflow: hidden; background: var(--bg); }
  .infographic { position: relative; width: 1200px; height: 1200px; font-family: "Catamaran", sans-serif; }

  .feature-disc {
    position: absolute;
    border-radius: 50%;
    background: radial-gradient(circle at 40% 35%, var(--disc-light), var(--disc-deep));
    transform: translate(-50%, -50%);
  }
  .feature-disc .rate {
    position: absolute;
    left: 50%;
    bottom: 14%;
    transform: translateX(-50%);
    font-family: "Poppins", sans-serif;
    font-weight: 800;
    font-size: 44px;
    line-height: 1;
    color: var(--badge);
    white-space: nowrap;
  }

  .feature-title, .feature-note, .main-heading {
    position: absolute;
    transform: translateX(-50%);
    text-align: center;
    white-space: nowrap;
  }
  .feature-title {
    font-weight: 700;
    font-size: 25px;
    letter-spacing: 0.09em;
    color: var(--accent);
    line-height: 26px;
  }
  .feature-note {
    font-weight: 400;
    font-size: 16px;
    letter-spacing: 0.08em;
    color: var(--body-text);
    line-height: 26px;
  }
  .main-heading {
    font-weight: 700;
    font-size: 40px;
    letter-spacing: 0.09em;
    color: var(--accent);
    line-height: 40px;
  }
</style>
</head>
<body>
<main class="infographic">

  <!-- Row 1 -->
  <div class="feature-disc" style="left:308px;top:202px;width:216px;height:216px" role="img" aria-label="3D-Illustration einer braunen Geldbörse mit Geldscheinen">
    <span class="rate">100%</span>
  </div>
  <h2 class="feature-title" style="left:306px;top:314px">Anonymität</h2>
  <p class="feature-note" style="left:303px;top:346px">Keine Rückschlüsse<br>auf Sie möglich</p>

  <div class="feature-disc" style="left:630px;top:192px;width:214px;height:214px" role="img" aria-label="3D-Illustration eines weißen Bankgebäudes mit Säulen"></div>
  <h2 class="feature-title" style="left:634px;top:311px">Vermögenssichenung</h2>
  <p class="feature-note" style="left:624px;top:343px">Immobilien Barvermögen<br>Auto Boot Flugzeug Uhren<br>Kryptowährung Firmenanteile</p>

  <div class="feature-disc" style="left:941px;top:194px;width:208px;height:208px" role="img" aria-label="3D-Illustration eines gebündelten Geldscheinstapels">
    <span class="rate">0%</span>
  </div>
  <h2 class="feature-title" style="left:948px;top:312px">Wegzugsbesteuerung</h2>
  <p class="feature-note" style="left:938px;top:342px">Freiheit</p>

  <h1 class="main-heading" style="left:641px;top:441px">Vermögensschutz</h1>

  <!-- Row 2 -->
  <div class="feature-disc" style="left:294px;top:608px;width:216px;height:216px" role="img" aria-label="3D-Illustration eines farbigen Tortendiagramms">
    <span class="rate">0%</span>
  </div>
  <h2 class="feature-title" style="left:292px;top:722px">Gunderwerbssteuer</h2>
  <p class="feature-note" style="left:292px;top:750px">freie Einbringung</p>

  <div class="feature-disc" style="left:629px;top:606px;width:224px;height:224px" role="img" aria-label="3D-Illustration eines dunkelgrauen Tresors"></div>
  <h2 class="feature-title" style="left:633px;top:722px">Legal und rechtssicher</h2>

  <div class="feature-disc" style="left:962px;top:597px;width:218px;height:218px" role="img" aria-label="3D-Illustration einer Dokumentrolle mit grünem Haken">
    <span class="rate">0%</span>
  </div>
  <h2 class="feature-title" style="left:966px;top:721px">Erbschaftssteuer</h2>

  <!-- Row 3 -->
  <div class="feature-disc" style="left:282px;top:952px;width:224px;height:224px" role="img" aria-label="3D-Illustration eines Kartenterminals mit Beleg"></div>
  <h2 class="feature-title" style="left:279px;top:1084px">Steueroptimierung</h2>
  <p class="feature-note" style="left:279px;top:1113px">für das laufende<br>Einkommen</p>

  <div class="feature-disc" style="left:620px;top:947px;width:222px;height:222px" role="img" aria-label="3D-Illustration eines blauen Geldsacks mit Goldmünzen"></div>
  <h2 class="feature-title" style="left:614px;top:1084px">Schutz</h2>
  <p class="feature-note" style="left:614px;top:1113px">vor Ansprüchen<br>Dritter</p>

  <div class="feature-disc" style="left:956px;top:951px;width:218px;height:218px" role="img" aria-label="3D-Illustration roter Münzstapel">
    <span class="rate">100%</span>
  </div>
  <h2 class="feature-title" style="left:951px;top:1079px">Insolvenz sicher</h2>
  <p class="feature-note" style="left:950px;top:1108px">Kein Zugriff vom<br>Insolvenzverwalter</p>

</main>
</body>
</html>
```